Business Card Design Project

I require a business card for a new coaching business based in Melbourne with global clients. Both companies and individuals will retain our coaching services.

Target Market(s)

Both small business and large corporate in western speaking countries. Individuals requiring support and direction on issues such as fears, phobias, career, relationships, confidence, self esteem etc.

Industry/Entity Type

Business

Font styles to use
Sans Serif

Colors

Designer to choose colors to be used in the design.

Requirements
Must have
• White background to enhance the colours in the logo. Logo on the left.
Should not have
• The black and white version of the logo. Keep the colours.

```html
<!DOCTYPE html>
<html lang="en">
<head>
<meta charset="utf-8">
<title>Clear Path Coaching – Business Card</title>
<link rel="stylesheet" href="https://fonts.googleapis.com/css2?family=Arimo:wght@400&display=swap">
<style>
  :root {
    --card-white: #ffffff;
    --band-lime: #dcdc52;
    --edge-lilac: #b9b5d8;
    --ink: #111111;
    --brand-grey: #6d6e71;
    --brand-dot: #f0922e;
    --link-violet: #5a3fd0;
  }
  html, body {
    margin: 0;
    padding: 0;
    width: 1200px;
    height: 686px;
    overflow: hidden;
    background: var(--card-white);
  }
  .card {
    position: relative;
    width: 1200px;
    height: 686px;
    background: var(--card-white);
    border-left: 3px solid var(--edge-lilac);
    box-sizing: border-box;
    overflow: hidden;
    font-family: "Arimo", "Helvetica Neue", Arial, sans-serif;
    color: var(--ink);
  }
  .top-band {
    position: absolute;
    left: 0;
    top: 0;
    width: 100%;
    height: 69px;
    background: var(--band-lime);
  }
  .brand-tab {
    position: absolute;
    left: 76px;
    top: 0;
    width: 573px;
    height: 230px;
    background: var(--card-white);
    border-radius: 28px 28px 0 0;
  }
  .brand {
    position: absolute;
    left: 135px;
    top: 48px;
    display: flex;
    align-items: center;
    gap: 26px;
  }
  .brand-dot {
    width: 150px;
    height: 150px;
    border-radius: 50%;
    background: var(--brand-dot);
    flex: none;
  }
  .brand-name {
    margin: 0;
    font-family: "Arimo", "Helvetica Neue", Arial, sans-serif;
    font-weight: 400;
    font-size: 42px;
    line-height: 46px;
    color: var(--brand-grey);
    text-transform: uppercase;
  }
  .holder {
    position: absolute;
    left: 680px;
    top: 160px;
    width: 500px;
  }
  .holder-name {
    margin: 0 0 30px;
    font-size: 35px;
    font-weight: 400;
    line-height: 1.2;
  }
  .holder-role {
    margin: 0;
    font-size: 35px;
    font-weight: 400;
    line-height: 59px;
  }
  .contact {
    position: absolute;
    left: 680px;
    top: 397px;
    margin: 0;
    font-size: 27px;
    line-height: 1;
  }
  .contact-row {
    display: flex;
    height: 73px;
  }
  .contact-label {
    width: 171px;
    margin: 0;
  }
  .contact-value {
    margin: 0;
  }
  .contact-value a {
    color: var(--link-violet);
    text-decoration: underline;
  }
</style>
</head>
<body>
  <div class="card">
    <div class="top-band"></div>
    <div class="brand-tab"></div>

    <div class="brand">
      <span class="brand-dot"></span>
      <p class="brand-name">Clear Path<br>Coaching</p>
    </div>

    <div class="holder">
      <h1 class="holder-name">Lena Marchetti-Hale</h1>
      <h2 class="holder-role">Performance Consultant and<br>Coach</h2>
    </div>

    <dl class="contact">
      <div class="contact-row">
        <dt class="contact-label">Phone</dt>
        <dd class="contact-value">+61 (0) 400 555 019</dd>
      </div>
      <div class="contact-row">
        <dt class="contact-label">Email</dt>
        <dd class="contact-value"><a href="mailto:lena.mh@example.com">lena.mh@example.com</a></dd>
      </div>
      <div class="contact-row">
        <dt class="contact-label">ABN</dt>
        <dd class="contact-value">51824603917</dd>
      </div>
    </dl>
  </div>
</body>
</html>
```